Album Single Song Cover Art Needed - Hip-Hop, Pop, R&B Artist

Need a CD "Single Release" Cover Art designed for Native American Hip Hop Artist - K Lumina. Template: Pressvault - 300ppi. Two separate Art Designs - One with no wording; the other with Wording. Single Song Title is: Night Tide / Artist: K Lumina. Thoughts on artwork - Close Up of Face, create a vision of "Fierce". Looking to make a powerful statement - colors vibrant, splashy. Let your creativity run free - whatever "FIERCE" comes to mind, etc., Let me see what you can do. I provided a couple of pictures - take your pick of any to use - remove background. Happy designing!
Updates

Would like to see a few more designs come through as well as allow you to create additional designs. Thank you.

Target Market(s)

Music, Entertainment

Industry/Entity Type

Music, Entertainment

Font styles to use
Other font styles liked:
• Let the Designer Choose

Requirements
Must have
• FIERCE
Nice to have
• Vibrant, Color, Splashes - think "FIERCE"

```html
<!DOCTYPE html>
<html lang="en">
<head>
<meta charset="utf-8">
<title>FIERCE – K Lumina</title>
<link rel="stylesheet" href="https://fonts.googleapis.com/css2?family=Anton&family=Oswald:wght@500&family=Teko:wght@600&display=swap">
<style>
  :root {
    --ink: #050505;
    --deep-navy: #15173f;
    --violet: #3a2a8a;
    --electric-blue: #1e7fe0;
    --sky: #3fc4f2;
    --sun-yellow: #ffe414;
    --flame-orange: #ff7a10;
    --hot-red: #e5141c;
    --magenta: #e0147f;
    --leaf-green: #17a03a;
    --olive: #3a3a08;
    --white: #ffffff;
  }
  * { margin: 0; padding: 0; box-sizing: border-box; }
  html, body {
    width: 1200px;
    height: 1200px;
    overflow: hidden;
    background: var(--ink);
  }
  .cover {
    position: relative;
    width: 1200px;
    height: 1200px;
    overflow: hidden;
  }
  .cover-artwork {
    position: absolute;
    inset: 0;
    background:
      radial-gradient(ellipse 26% 20% at 44% 56%, var(--ink) 0, rgba(5,5,5,0.85) 55%, rgba(5,5,5,0) 100%),
      radial-gradient(ellipse 30% 32% at 30% 22%, rgba(10,10,25,0.95) 0, rgba(10,10,25,0) 100%),
      radial-gradient(ellipse 16% 20% at 4% 20%, rgba(255,228,20,0.8) 0, rgba(255,228,20,0) 100%),
      radial-gradient(ellipse 22% 30% at 100% 26%, var(--sky) 0, rgba(63,196,242,0) 100%),
      conic-gradient(from 0deg at 46% 52%,
        var(--deep-navy) 0deg,
        var(--violet) 20deg,
        var(--electric-blue) 40deg,
        var(--sky) 58deg,
        var(--leaf-green) 72deg,
        var(--sun-yellow) 86deg,
        var(--flame-orange) 102deg,
        var(--hot-red) 122deg,
        #2a0606 150deg,
        var(--hot-red) 172deg,
        #1a1a1a 190deg,
        var(--electric-blue) 210deg,
        var(--magenta) 228deg,
        var(--sun-yellow) 244deg,
        var(--leaf-green) 262deg,
        var(--hot-red) 278deg,
        var(--olive) 300deg,
        var(--sun-yellow) 312deg,
        var(--olive) 328deg,
        var(--ink) 345deg,
        var(--deep-navy) 360deg);
  }
  .cover-type {
    position: absolute;
    inset: 0;
    width: 1200px;
    height: 1200px;
  }
  .title {
    font-family: "Anton", sans-serif;
    font-size: 400px;
    fill: url(#title-fill);
    stroke: var(--ink);
    stroke-width: 10px;
    stroke-linejoin: round;
    paint-order: stroke fill;
    filter: drop-shadow(-12px 14px 0 var(--ink));
  }
  .tagline {
    font-family: "Oswald", sans-serif;
    font-weight: 500;
    font-size: 46px;
    fill: var(--white);
    stroke: var(--ink);
    stroke-width: 4px;
    paint-order: stroke fill;
  }
  .artist-name {
    font-family: "Teko", sans-serif;
    font-weight: 600;
    font-size: 104px;
    fill: var(--white);
    filter: drop-shadow(-4px 4px 0 var(--ink));
  }
</style>
</head>
<body>
  <main class="cover">
    <div class="cover-artwork" role="img" aria-label="Close-up of the artist's face, mouth open in a fierce shout, bursting with vibrant splashes of yellow, blue, green, orange, red and magenta paint on a dark background"></div>
    <svg class="cover-type" viewBox="0 0 1200 1200" aria-labelledby="cover-title">
      <defs>
        <linearGradient id="title-fill" x1="0" y1="0" x2="1" y2="0">
          <stop offset="0" stop-color="#ffffff"/>
          <stop offset="0.2" stop-color="#cfefff"/>
          <stop offset="0.45" stop-color="#fff6b0"/>
          <stop offset="0.62" stop-color="#ffe414"/>
          <stop offset="0.78" stop-color="#ffffff"/>
          <stop offset="1" stop-color="#ffe414"/>
        </linearGradient>
      </defs>
      <text id="cover-title" class="title" x="100" y="1100" textLength="1100" lengthAdjust="spacingAndGlyphs" transform="rotate(-15 100 1100)">FIERCE</text>
      <text class="tagline" x="347" y="1129" textLength="745" lengthAdjust="spacingAndGlyphs" transform="rotate(-16.6 347 1129)">NATIVE AMERICAN HIP HOP ARTIST</text>
      <text class="artist-name" x="598" y="1138" textLength="275" lengthAdjust="spacingAndGlyphs" transform="rotate(-14.7 598 1138)">K LUMINA</text>
    </svg>
  </main>
</body>
</html>
```